Company or website name
- Dr. Renaud Vasquelle
- Links to the website
- Retired doctor; professional speaker, Life coach, author, healthcare consultant
- Other Facts

```html
<!DOCTYPE html>
<html lang="en">
<head>
<meta charset="utf-8">
<title>Dr. Renaud Vasquelle – Coaching and Consulting</title>
<link rel="stylesheet" href="https://fonts.googleapis.com/css2?family=Open+Sans:wght@300;400;700&family=Roboto+Condensed:wght@300;400&display=swap">
<style>
  :root {
    --brand-blue: #0a86d3;
    --panel-blue: #1488d6;
    --band-grey: #c6c6c6;
    --ribbon-yellow: #dbe33a;
    --ribbon-shadow: #8f8f8f;
    --accent-lime: #dfee2e;
    --white: #ffffff;
    --ink: #111111;
    --tab-cap: #4d4d4d;
    --photo-light: #e9eaee;
    --photo-mid: #b9bcc6;
    --photo-dark: #3a3a40;
  }
  * { box-sizing: border-box; margin: 0; padding: 0; }
  html, body { width: 1200px; height: 900px; overflow: hidden; background: var(--white); }
  body { font-family: "Open Sans", Arial, sans-serif; }

  .page { position: relative; width: 1200px; height: 900px; background: var(--white); }

  /* Header */
  .site-header { position: absolute; left: 0; top: 0; width: 1200px; height: 117px; background: var(--brand-blue); }
  .brand { position: absolute; left: 70px; top: 22px; display: flex; align-items: flex-start; gap: 14px; color: var(--white); }
  .brand-dot { width: 46px; height: 46px; border-radius: 50%; background: var(--white); margin-top: 8px; }
  .brand-name { font-weight: 300; font-size: 52px; line-height: 56px; letter-spacing: -1px; }
  .brand-tagline { font-weight: 300; font-size: 15px; letter-spacing: 2px; margin-top: 2px; padding-left: 10px; }

  .nav-home { position: absolute; left: 1038px; top: 76px; width: 78px; height: 56px; }
  .nav-home .cap { position: absolute; left: 0; top: 0; width: 78px; height: 5px; background: var(--tab-cap); }
  .nav-home a { position: absolute; left: 2px; top: 3px; width: 74px; height: 53px; background: var(--brand-blue);
    clip-path: polygon(0 0, 100% 0, 100% 100%, 50% 78%, 0 100%);
    color: var(--white); font-weight: 700; font-size: 16px; letter-spacing: 1px; text-align: center; padding-top: 9px; text-decoration: none; }
  .nav-rule { position: absolute; left: 1116px; top: 129px; width: 56px; height: 2px; background: #9c9c9c; }

  /* Purpose band */
  .purpose-band { position: absolute; left: 0; top: 127px; width: 1200px; height: 379px; background: var(--band-grey); }
  .purpose-label { position: absolute; left: 59px; top: 28px; width: 357px; height: 42px; }
  .purpose-label .cap { position: absolute; left: 0; top: 0; width: 4px; height: 42px; background: var(--tab-cap); }
  .purpose-label h2 { position: absolute; left: 4px; top: 0; width: 353px; height: 42px; background: var(--brand-blue);
    clip-path: polygon(0 0, 100% 0, 93% 50%, 100% 100%, 0 100%);
    color: var(--accent-lime); font-weight: 400; font-size: 25px; line-height: 42px; padding-left: 20px; }
  .purpose-text { position: absolute; left: 30px; top: 68px; width: 710px; text-align: center;
    color: var(--white); font-weight: 300; font-size: 26px; line-height: 33.5px; }

  .speaker-tag { position: absolute; left: 381px; top: 271px; width: 463px; height: 74px; }
  .speaker-tag .cap { position: absolute; right: 0; top: -12px; width: 5px; height: 96px; background: var(--tab-cap); }
  .speaker-tag .face { position: absolute; left: 0; top: 0; width: 458px; height: 74px; background: var(--brand-blue);
    clip-path: polygon(0 0, 100% 0, 100% 100%, 0 100%, 8% 50%); padding: 6px 0 0 62px; }
  .speaker-name { color: var(--accent-lime); font-weight: 700; font-size: 27px; line-height: 32px; letter-spacing: 2px; }
  .speaker-role { color: var(--white); font-weight: 400; font-size: 19.5px; line-height: 24px; }

  .speaker-photo { position: absolute; left: 866px; top: 13px; width: 316px; height: 366px;
    background: linear-gradient(180deg, var(--photo-light) 0%, var(--photo-mid) 50%, var(--photo-dark) 100%);
    border-radius: 110px 110px 0 0; }

  /* Resource panel */
  .resource-panel { position: absolute; left: 59px; top: 506px; width: 1081px; height: 352px; background: var(--panel-blue); }

  .ribbon { position: absolute; height: 46px; width: 362px; }
  .ribbon .fold { position: absolute; top: 38px; width: 28px; height: 16px; background: var(--ribbon-shadow); }
  .ribbon a { position: absolute; top: 0; width: 362px; height: 39px; background: var(--ribbon-yellow);
    color: var(--panel-blue); font-family: "Roboto Condensed", "Arial Narrow", sans-serif; font-weight: 300;
    font-size: 27px; line-height: 39px; letter-spacing: 1px; text-decoration: none; white-space: nowrap; }
  .ribbon-left { left: 33px; }
  .ribbon-left .fold { left: 0; clip-path: polygon(0 0, 100% 0, 100% 100%); }
  .ribbon-left a { left: 0; padding-left: 34px; clip-path: polygon(0 0, 100% 0, 94% 50%, 100% 100%, 0 100%); }
  .ribbon-right { left: 806px; }
  .ribbon-right .fold { right: 0; clip-path: polygon(0 0, 100% 0, 0 100%); }
  .ribbon-right a { left: 0; padding-right: 32px; text-align: right; clip-path: polygon(0 0, 100% 0, 100% 100%, 0 100%, 6% 50%); }

  .resource-intro { position: absolute; left: 424px; top: 570px; width: 348px; text-align: center;
    color: var(--white); font-weight: 700; font-size: 14.5px; line-height: 28px; letter-spacing: 0.8px; }

  .site-footer { position: absolute; left: 0; top: 860px; width: 1200px; text-align: center;
    color: var(--ink); font-weight: 700; font-size: 15px; letter-spacing: 0.8px; }
</style>
</head>
<body>
<div class="page">
  <header class="site-header">
    <div class="brand">
      <span class="brand-dot"></span>
      <div>
        <div class="brand-name">Vasquelle</div>
        <div class="brand-tagline">coaching and consulting</div>
      </div>
    </div>
    <nav class="nav-home"><span class="cap"></span><a href="#">Home</a></nav>
  </header>
  <div class="nav-rule"></div>

  <section class="purpose-band">
    <div class="purpose-label"><span class="cap"></span><h2>My Purpose Statement:</h2></div>
    <p class="purpose-text">"I commit my working life to care, respect and<br>practical help for the good of every person I meet.<br>I do this by guiding people toward their strengths,<br>through books, talks and one-to-one coaching;<br>turning everyday people into confident,<br>purpose-led individuals"</p>
    <div class="speaker-tag">
      <span class="cap"></span>
      <div class="face">
        <div class="speaker-name">Renaud Vasquelle</div>
        <div class="speaker-role">Professional Speaker, Author, Life Coach</div>
      </div>
    </div>
    <div class="speaker-photo" role="img" aria-label="Portrait photo of the speaker in a shirt, striped tie and dark vest"></div>
  </section>

  <section class="resource-panel"></section>

  <nav class="resource-links">
    <div class="ribbon ribbon-left" style="top:526px"><span class="fold"></span><a href="#">The Daily Spark</a></div>
    <div class="ribbon ribbon-left" style="top:589px"><span class="fold"></span><a href="#">Words of Wisdom</a></div>
    <div class="ribbon ribbon-left" style="top:655px"><span class="fold"></span><a href="#">Available Seminar Topics</a></div>
    <div class="ribbon ribbon-left" style="top:716px"><span class="fold"></span><a href="#">Plain Wisdom Series</a></div>
    <div class="ribbon ribbon-left" style="top:787px"><span class="fold"></span><a href="#">Videos</a></div>

    <div class="ribbon ribbon-right" style="top:526px"><span class="fold"></span><a href="#">Building Your Bright Life</a></div>
    <div class="ribbon ribbon-right" style="top:589px"><span class="fold"></span><a href="#">About Your Speaker</a></div>
    <div class="ribbon ribbon-right" style="top:655px"><span class="fold"></span><a href="#">Want Coaching?</a></div>
    <div class="ribbon ribbon-right" style="top:716px"><span class="fold"></span><a href="#">Booking Renaud</a></div>
    <div class="ribbon ribbon-right" style="top:785px"><span class="fold"></span><a href="#">Contact Us</a></div>
  </nav>

  <p class="resource-intro">The information found on this website is intended to inspire you to achieve your full potential. There are a variety of resources including the Daily Spark, the Plain Wisdom Series, Building Your Bright Life, and many other great resources to help make every day a terrific day!</p>

  <footer class="site-footer">Copyright © Dr. Renaud A. Vasquelle,2013</footer>
</div>
</body>
</html>
```